依頼詳細
「企業ロゴ」が黒と黄色のため、基本的なカラーリングベースは、黒色で黄色のあしらいやワンポイントカラーを入れるイメージを持っております。
デザインイメージは、「未来的」「先進的」などを強く主張したいと思っております。

本件は、Topページのみのテストとして、「コンペ形式」となりますが、
当選された場合には、約10ページほどの下層ページのご依頼も約束させて頂きます。
(予算は10万円前後)
さらに、今後の案件にて、「継続的」に案件を斡旋させて頂きたいと思っておりますので、
末長くお付き合いして頂けると幸いです。
また、当選後は、デザインに利用したファイルやデータを提出して頂きたいです。

```html
<!DOCTYPE html>
<html lang="ja">
<head>
<meta charset="UTF-8">
<title>Nexaline</title>
<link rel="stylesheet" href="https://fonts.googleapis.com/css2?family=Inter:wght@400;500;700;800&family=Noto+Sans+JP:wght@400;500;700&display=swap">
<style>
:root{
  --yellow:#f2ea37;
  --black:#0b0b0b;
  --white:#ffffff;
  --grey:#9c9c9c;
  --ink:#1a1a1a;
  --muted:#555;
}
*{box-sizing:border-box;margin:0;padding:0}
html,body{width:1200px;height:4416px;overflow:hidden}
body{font-family:"Inter","Noto Sans JP",sans-serif;color:var(--ink);background:var(--white);position:relative}
.jp{font-family:"Noto Sans JP",sans-serif}
.pill{display:inline-block;background:var(--black);color:var(--white);border-radius:30px;font-size:11px;font-weight:700;padding:12px 30px;font-family:"Noto Sans JP",sans-serif}
.pill.light{background:var(--white);color:var(--black)}

/* header + hero */
.top{position:absolute;left:0;top:0;width:1200px;height:448px;overflow:hidden}
.top .waves{position:absolute;left:380px;top:-40px;width:700px;height:380px;
  background:radial-gradient(ellipse at 50% 40%,rgba(242,234,55,.85),rgba(242,234,55,.35) 45%,rgba(242,234,55,0) 70%)}
.header{position:absolute;left:0;top:0;width:1200px;height:70px;display:flex;align-items:center;justify-content:space-between;padding:0 30px 0 124px}
.brand{display:flex;align-items:center;gap:8px;font-weight:800;font-size:20px;color:var(--black)}
.brand .dot{width:12px;height:12px;background:var(--yellow);border-radius:50%}
.nav{display:flex;gap:30px;align-items:center;font-size:11px;font-weight:700;letter-spacing:.04em}
.nav .pill{padding:8px 20px;font-family:"Inter",sans-serif}
.hero-title{position:absolute;left:124px;top:184px;font-size:74px;font-weight:800;letter-spacing:-.02em;color:var(--black)}
.hero-lead{position:absolute;left:124px;top:292px;font-size:14px;line-height:1.9;color:var(--ink)}
.hero-photo{position:absolute;left:0;top:448px;width:1200px;height:672px;
  background:linear-gradient(180deg,#5a6d86 0%,#3e4f66 45%,#28323f 100%)}
.scroll{position:absolute;right:34px;top:380px;width:18px;height:140px;background:#222;border-radius:10px;color:#fff;font-size:8px;writing-mode:vertical-rl;text-align:center;line-height:18px;letter-spacing:.2em}

/* about */
.about{position:absolute;left:0;top:1120px;width:1200px;height:600px;overflow:hidden}
.about .ghost{position:absolute;left:0;top:300px;width:1200px;text-align:center;font-size:210px;font-weight:800;letter-spacing:-.02em;color:transparent;-webkit-text-stroke:1.5px rgba(0,0,0,.08);line-height:1}
.about .circle{position:absolute;left:222px;top:20px;width:756px;height:560px;border-radius:50%;background:var(--yellow)}
.about .body{position:absolute;left:370px;top:110px;width:470px}
.about .eyebrow{font-size:16px;font-weight:700}
.about h2{font-size:48px;font-weight:800;line-height:1.12;margin-top:14px;letter-spacing:-.01em}
.about p{font-size:11px;line-height:2;margin-top:34px;color:#333}
.about .pill{margin-top:34px;margin-left:160px}

/* services */
.services{position:absolute;left:0;top:1720px;width:1200px;height:672px;display:flex}
.svc{position:relative;width:400px;height:672px;color:var(--white)}
.svc.web{background:linear-gradient(160deg,#b9bcc0,#6d7075 60%,#3f4246)}
.svc.free{background:linear-gradient(180deg,#f3f3f1 0%,#c8c6c0 50%,#6f6a63 100%)}
.svc.event{background:linear-gradient(160deg,#cfd0cc,#7c7e7a 55%,#3b3d3c)}
.svc .shade{position:absolute;inset:0;background:rgba(0,0,0,.28)}
.svc.free .shade{background:rgba(0,0,0,.18)}
.svc .txt{position:absolute;left:50px;top:226px}
.svc .jp{font-size:15px;font-weight:700;color:var(--yellow)}
.svc h3{font-size:46px;font-weight:800;line-height:1.05;margin-top:6px;letter-spacing:-.01em}
.svc .go{position:absolute;right:40px;top:508px;width:34px;height:34px;border-radius:50%;background:var(--black);display:flex;align-items:center;justify-content:center}
.services .label{position:absolute;left:400px;top:134px;width:400px;text-align:center;font-size:20px;font-weight:800;color:var(--black)}

/* news */
.news{position:absolute;left:0;top:2392px;width:1200px;height:448px;background:var(--black);color:var(--white)}
.news h2{position:absolute;left:156px;top:132px;font-size:28px;font-weight:800}
.news .pill{position:absolute;left:130px;top:228px;padding:8px 22px;font-size:10px}
.news ul{position:absolute;left:360px;top:128px;width:720px;list-style:none}
.news li{display:flex;align-items:center;height:75px;border-bottom:1px solid #333;font-size:11px}
.news li:first-child{border-top:1px solid #333}
.news li .date{width:150px;padding-left:10px;color:#bbb}
.news li .t{flex:1}
.news li .plus{width:30px;text-align:center;font-size:16px}

/* recruit */
.recruit{position:absolute;left:0;top:2840px;width:1200px;height:680px;background:linear-gradient(120deg,#4a525c 0%,#9aa1a8 40%,#c5c9cc 55%,#6b727a 100%)}
.recruit .veil{position:absolute;inset:0;background:rgba(255,255,255,.25)}
.recruit .body{position:absolute;left:482px;top:132px;width:500px}
.recruit .label{font-size:20px;font-weight:800;margin-left:50px}
.recruit .eyebrow{font-size:16px;font-weight:700;margin-top:24px}
.recruit h2{font-size:46px;font-weight:800;line-height:1.12;margin-top:10px;color:var(--black)}
.recruit p{font-size:11px;line-height:2;margin-top:28px;color:#222;width:470px}
.recruit .pill{margin-top:40px;margin-left:50px}

/* contact */
.contact{position:absolute;left:0;top:3520px;width:1200px;height:400px;background:var(--yellow);overflow:hidden}
.contact .wave{position:absolute;left:200px;top:170px;width:800px;height:150px;background:radial-gradient(ellipse at 50% 50%,rgba(0,0,0,.35),rgba(0,0,0,0) 65%)}
.contact .label{position:absolute;left:0;top:98px;width:1200px;text-align:center;font-size:22px;font-weight:800}
.contact .cta{position:absolute;left:212px;top:186px;font-size:58px;font-weight:800;letter-spacing:-.01em;color:var(--black);display:flex;align-items:center;gap:16px;border-bottom:5px solid var(--black);padding-bottom:6px}
.badge{position:absolute;left:1134px;top:3900px;width:44px;height:44px;border-radius:50%;background:var(--black);border:3px solid var(--yellow)}

/* footer */
.footer{position:absolute;left:0;top:3920px;width:1200px;height:496px;background:var(--grey);overflow:hidden}
.footer .glow{position:absolute;left:420px;top:300px;width:480px;height:360px;border-radius:50%;background:radial-gradient(circle,rgba(242,234,55,1) 0%,rgba(242,234,55,.6) 40%,rgba(242,234,55,0) 70%)}
.footer h2{position:absolute;left:130px;top:68px;font-size:40px;font-weight:800;line-height:1.1;color:var(--black)}
.footer .co{position:absolute;left:880px;top:68px;font-size:10px;line-height:1.8;color:#222}
.footer .co b{font-size:12px}
.footer .links{position:absolute;left:130px;top:272px;display:flex;gap:42px;font-size:9px;color:#111}
.footer .links div{line-height:2}
.footer .copy{position:absolute;left:0;top:424px;width:1200px;text-align:center;font-size:9px;color:#222}
</style>
</head>
<body>

<section class="top">
  <div class="waves" role="img" aria-label="Flowing yellow line pattern"></div>
  <header class="header">
    <div class="brand"><span>Nexaline</span><span class="dot"></span></div>
    <nav class="nav">
      <span>SERVICE</span><span>COMPANY</span><span>NEWS</span><span>RECRUIT</span>
      <span class="pill">CONTACT ›</span>
    </nav>
  </header>
  <h1 class="hero-title">Catchphrase Goes Here.</h1>
  <p class="hero-lead jp">ここに説明文が入ります。ここに説明文が入ります。<br>ここに説明文が入ります。ここに説明文が入ります。ここに説明文が入ります。</p>
</section>
<div class="hero-photo" role="img" aria-label="City skyline of office towers at dusk"></div>
<div class="scroll">SCROLL</div>

<section class="about">
  <div class="ghost">Nexaline</div>
  <div class="circle"></div>
  <div class="body">
    <div class="eyebrow jp">わたしたちが全力でサポートします。</div>
    <h2>We Do Our Best To<br>Support You.</h2>
    <p class="jp">ここに説明文が入ります。ここに説明文が入ります。ここに説明文が入ります。ここに説明文が入ります。ここに説明文が入ります。ここに説明文が入ります。ここに説明文が入ります。ここに説明文が入ります。ここに説明文が入ります。ここに説明文が入ります。ここに説明文が入ります。</p>
    <span class="pill">会社概要を見る</span>
  </div>
</section>

<section class="services">
  <div class="svc web" role="img" aria-label="Hands working at a laptop and tablet">
    <div class="shade"></div>
    <div class="txt"><div class="jp">Web制作</div><h3>Web Create</h3></div>
    <div class="go"><svg width="10" height="10" viewBox="0 0 10 10"><path d="M3 1l4 4-4 4" stroke="#fff" stroke-width="1.5" fill="none"/></svg></div>
  </div>
  <div class="svc free" role="img" aria-label="Team members standing in an office">
    <div class="shade"></div>
    <div class="txt"><div class="jp">フリーランス支援</div><h3>Freelance<br>Support</h3></div>
    <div class="go"><svg width="10" height="10" viewBox="0 0 10 10"><path d="M3 1l4 4-4 4" stroke="#fff" stroke-width="1.5" fill="none"/></svg></div>
  </div>
  <div class="svc event" role="img" aria-label="Guests talking at an event">
    <div class="shade"></div>
    <div class="txt"><div class="jp">イベント企画・運営</div><h3>Event<br>Planning &amp;<br>Management</h3></div>
    <div class="go"><svg width="10" height="10" viewBox="0 0 10 10"><path d="M3 1l4 4-4 4" stroke="#fff" stroke-width="1.5" fill="none"/></svg></div>
  </div>
  <div class="label">OUR SERVICES</div>
</section>

<section class="news">
  <h2>NEWS</h2>
  <span class="pill light">ニュース一覧を見る</span>
  <ul class="jp">
    <li><span class="date">2024.01.20</span><span class="t">新サービスのお知らせを公開しました</span><span class="plus">+</span></li>
    <li><span class="date">2024.01.12</span><span class="t">イベント開催のご案内を掲載しました</span><span class="plus">+</span></li>
    <li><span class="date">2024.01.05</span><span class="t">年始営業のお知らせ</span><span class="plus">+</span></li>
  </ul>
</section>

<section class="recruit" role="img" aria-label="Business handshake between two people">
  <div class="veil"></div>
  <div class="body">
    <div class="label">RECRUIT</div>
    <div class="eyebrow jp">わたしたちといっしょに働きませんか？</div>
    <h2>How Is That<br>Working With Us?</h2>
    <p class="jp">ここに説明文が入ります。ここに説明文が入ります。ここに説明文が入ります。ここに説明文が入ります。ここに説明文が入ります。ここに説明文が入ります。ここに説明文が入ります。ここに説明文が入ります。</p>
    <span class="pill">採用情報を見る</span>
  </div>
</section>

<section class="contact">
  <div class="wave" role="img" aria-label="Flowing dark line pattern"></div>
  <div class="label">CONTACT</div>
  <a class="cta">Click Here To Contact Us.
    <svg width="44" height="44" viewBox="0 0 44 44"><path d="M8 36L36 8M14 8h22v22" stroke="#0b0b0b" stroke-width="5" fill="none"/></svg>
  </a>
</section>

<footer class="footer">
  <div class="glow"></div>
  <h2>Catchphrase Goes<br>Here.</h2>
  <div class="co jp"><b>Nexaline株式会社</b><br>〒100-0000 東京都架空区見本町1-2-3<br>TEL 00-0000-0000 / FAX 00-0000-0001</div>
  <div class="links jp">
    <div>トップ</div>
    <div>事業内容<br>- Web制作<br>- フリーランス支援<br>- イベント企画・運営</div>
    <div>会社概要</div>
    <div>新着ニュース</div>
    <div>採用情報</div>
    <div>お問い合わせ</div>
    <div style="margin-left:60px">プライバシーポリシー</div>
    <div>サイトマップ</div>
  </div>
  <div class="copy">© 2024 Nexaline</div>
</footer>
<div class="badge"></div>

</body>
</html>
```